One of Australia's fastest growing energy maintenance contractors needs a new website

www.brightpane.com.au
Our business has evolved over the past years and now our website is no longer relevant.
We clean solar panels and we vacuum roof gutters.
We clean solar panels on the roofs of residential houses right up to billion dollar solar farms with in excess of 1 million panels. We offer thermal image testing and bird proofing for our residential and commercial clients and thermal drone imaging services for our solar farm clients.
We vacuum clean roof gutters (using a LoftSuk) on the residential house next door right up to enormous private and public schools, colleges, shopping centres, strat complexes and commercial buildings.
When first built our business had more of a domestic residential skew and the website reflected that. While that is still part of our core business we are now bidding on and have secured large government, commercial and infrastructure contracts and our new website needs to reflect our growth and our new business. We need a new site that it optimised for both desktop ad phone viewing as our latest figures showed that 73% of people visiting our site are on mobile phones. We have an extensive amount of data on Vesti Metrics available as well as Promos. Both that would also need integrating with the site along with a few other plugins such as Qarlo Chat Desk, Pallio etc along with SEO key words etc. We are also the winner and finalists over multiple years of the small business of the year awards and we like to proudly and prominently display those on our site.
We are looking for a new site with a modern professional feel / theme
There is a definitive break in our business between the solar Panel cleaning clients and the gutter cleaning clients so we would like a home page that begins with a simple choice:
Solar Panel Cleaning – Gutter Cleaning
With a professional full screen background image (we have hundreds to choose from) and along the bottom a small area with rights reserved etc, phone number etc (at some point in the future we will split these into two businesses but for now it’s what we have).
After that selection is made we would like a repeat of that same scenario but the selection is:
If it’s Solar Panel Cleaning
(new background image)
Government – Infrastructure – Commercial – Residential
If it’s Gutter Cleaning
(new background image)
Government – Strata – Commercial – Residential
After making those choices then onto the relevant pages with background images relevant to each sector and a them that suits (on the residential we would like to keep the link to our vesti ratings) - We will provide copy / text for each relevant page.
Other than that, a menu inclusive of the above and:
Resellers Portal – we will provide a link to this from Qarlo CRM)
Customer portal (we will supply a link to this from our booking system)
We also need a page for our Solar Resellers / Partners page but we will give them a link to this, it won’t be listed on the site.
Request a quote page (Again we will provide information from Qarlo as this will be linked to the CRM)
Standard contact us page inclusive of phone numbers, address and fields supplied from CRM
Sydney – 02 7391 5083
Southern Highlands – 02 4860 3178
Goulburn – 02 4860 3178
Canberra – 02 6172 8354
Wollongong – 02 4239 6017
sales@brightpane.com.au
Head Office - Ferndale Rise NSW 2590
ABN: 48906237115
Responsive Design: Optimized for desktop and mobile (73% mobile visitors).
Fast Loading Speed: Optimized for performance.
Smooth Transition Animations: For service and category selection.
Sticky Contact Bar: Always accessible at the bottom of mobile screens for quick calls.
SEO Optimization: Focused on government tenders, large-scale commercial contracts, and infrastructure projects.
Integrations
Vesti Metrics & Vesti Promos.
Qarlo Chat Desk.
Pallio Beacon.
SEO tools and keyword optimization.
Many many more images available if needed

```html
<!DOCTYPE html>
<html lang="en">
<head>
<meta charset="utf-8">
<title>BrightPane – Expert Cleaning Solutions</title>
<link rel="stylesheet" href="https://fonts.googleapis.com/css2?family=Poppins:wght@300;400;500;600;700&display=swap">
<style>
:root{
  --navy:#0b1c36;
  --navy-2:#11284a;
  --blue:#29b2e9;
  --blue-dark:#1a8ec4;
  --sky:#d7eefa;
  --sky-2:#eaf6fd;
  --ink:#1b2a3f;
  --muted:#5d6b7e;
  --white:#ffffff;
  --orange:#e9772c;
}
*{box-sizing:border-box;margin:0;padding:0}
html,body{width:1200px;height:4408px;overflow:hidden}
body{font-family:"Poppins",sans-serif;color:var(--ink);background:var(--white);position:relative}
.abs{position:absolute}
.ph{position:absolute}

/* header */
.topbar{left:380px;top:0;width:720px;height:34px;background:var(--navy);border-radius:0 0 0 18px;display:flex;align-items:center;justify-content:space-around;color:var(--white);font-size:13px;z-index:3}
.topbar span{display:flex;align-items:center;gap:6px}
.nav{left:0;top:34px;width:1200px;height:72px;display:flex;align-items:center;padding:0 60px;z-index:3}
.brand{display:flex;align-items:center;gap:10px;color:var(--white);font-weight:600;font-size:26px}
.brand-mark{width:28px;height:28px;background:var(--white);border-radius:4px}
.menu{display:flex;gap:26px;margin-left:120px;color:var(--white);font-size:14px}
.menu a{color:inherit;text-decoration:none}
.btn-contact{margin-left:auto;background:var(--blue);color:var(--white);padding:10px 20px;font-size:14px;border-radius:2px}

/* hero */
.hero{left:0;top:0;width:1200px;height:760px;background:linear-gradient(160deg,#2c5a86 0%,#1b3b63 45%,#0f2747 100%)}
.hero-shade{left:0;top:0;width:1200px;height:760px;background:linear-gradient(180deg,rgba(8,22,45,.35),rgba(8,22,45,.55))}
.hero h1{left:0;top:232px;width:1200px;text-align:center;color:var(--white);font-weight:600;font-size:64px;line-height:1.1}
.hero h1 small{display:block;font-size:44px;font-weight:400}
.hero .choose{left:0;top:508px;width:1200px;text-align:center;color:var(--white);font-size:28px;font-weight:500}
.choice{top:574px;height:46px;display:flex;align-items:center;justify-content:center;color:var(--white);font-size:15px;font-weight:500;width:200px}
.choice.gutter{left:394px;background:var(--navy)}
.choice.solar{left:610px;width:210px;background:var(--blue)}

/* about */
.about-bg{left:0;top:760px;width:1200px;height:700px;background:var(--white)}
.about-tint{left:0;top:1240px;width:1200px;height:640px;background:var(--sky);clip-path:polygon(0 25%,100% 0,100% 100%,0 100%)}
.hex{clip-path:polygon(25% 0,75% 0,100% 50%,75% 100%,25% 100%,0 50%)}
.hex-frame{left:70px;top:810px;width:470px;height:420px;background:var(--blue)}
.hex-photo-a{left:82px;top:822px;width:446px;height:396px;background:linear-gradient(140deg,#8fb6d8,#4c7fad 50%,#2e5f8a)}
.hex-photo-b{left:390px;top:1060px;width:230px;height:200px;background:linear-gradient(140deg,#6a9a6e,#3f6f8e)}
.hex-small{width:44px;height:38px;background:var(--blue)}
.eyebrow{font-size:14px;color:var(--muted);display:flex;align-items:center;gap:8px}
.eyebrow::before{content:"";width:30px;height:1px;background:var(--muted)}
.about-title{left:616px;top:918px;font-size:56px;font-weight:400;color:var(--navy);line-height:1}
.about-title b{font-weight:600}
.about-text{left:616px;top:996px;width:500px;font-size:14px;line-height:1.6;color:var(--muted)}
.about-text p+p{margin-top:12px}
.read-more{left:616px;top:1166px;font-size:14px;color:var(--navy);display:flex;align-items:center;gap:10px}
.read-more i{width:22px;height:22px;border-radius:50%;background:var(--blue);display:inline-block}

/* quote */
.quote-band{left:0;top:1460px;width:860px;height:370px;background:var(--navy);clip-path:polygon(0 0,92% 0,100% 100%,0 100%)}
.quote-tab{left:0;top:1476px;width:640px;height:58px;background:var(--navy-2);border-bottom:2px solid var(--blue)}
.quote-title{left:120px;top:1490px;color:var(--white);font-size:24px;font-weight:600}
.quote-list{left:120px;top:1556px;list-style:none;color:var(--white);font-size:14px}
.quote-list li{display:flex;align-items:center;gap:10px;height:30px}
.connect{left:120px;top:1660px;color:var(--white);font-size:22px;font-weight:600}
.connect-mail{left:120px;top:1702px;color:#c9d6e6;font-size:14px;display:flex;gap:8px;align-items:center}
.offices{left:120px;top:1736px;display:flex;gap:90px;color:var(--white);font-size:15px}
.offices div span{display:block;color:#c9d6e6;font-size:13px;margin-top:6px}
.worker{left:690px;top:1200px;width:300px;height:630px;background:linear-gradient(180deg,#c66b2c 0%,#e07a34 40%,#1d3457 75%,#15294a 100%);border-radius:140px 140px 0 0}

/* portals */
.portals{left:0;top:1830px;width:1200px;height:650px;background:var(--navy)}
.portals h2{left:0;top:1906px;width:1200px;text-align:center;color:var(--white);font-size:46px;font-weight:400}
.portals h2 b{font-weight:600}
.portals .sub{left:0;top:1972px;width:1200px;text-align:center;color:#c4d0de;font-size:14px}
.oct{clip-path:polygon(30% 0,70% 0,100% 30%,100% 70%,70% 100%,30% 100%,0 70%,0 30%)}
.portal-img{top:2020px;width:270px;height:300px}
.portal-img.customer{left:250px;background:linear-gradient(160deg,#d8dbe0,#8f9aa8 60%,#4b5b70)}
.portal-img.reseller{left:650px;background:linear-gradient(160deg,#e8d9c7,#b88f6d 55%,#5a4a45)}
.portal-name{top:2338px;width:380px;text-align:center;color:var(--white);font-size:22px;font-weight:600}
.portal-desc{top:2378px;width:380px;text-align:center;color:#c4d0de;font-size:13px;line-height:1.5}

/* testimonials */
.testi{left:0;top:2480px;width:1200px;height:610px;background:var(--sky)}
.testi-eyebrow{left:0;top:2530px;width:1200px;display:flex;justify-content:center;font-size:14px;color:var(--muted);gap:8px;align-items:center}
.testi h2{left:0;top:2570px;width:1200px;text-align:center;font-size:48px;font-weight:400;color:var(--navy)}
.testi h2 b{font-weight:600;color:var(--blue-dark)}
.t-card{top:2660px;width:340px;height:380px;background:var(--white);padding:110px 40px 0}
.t-card .avatar{position:absolute;left:140px;top:28px;width:60px;height:60px;border-radius:50%;background:linear-gradient(160deg,#c7d4e2,#7f93aa)}
.t-card h3{font-size:22px;font-weight:500;text-align:center;color:var(--navy)}
.t-card p{font-size:17px;text-align:center;margin-top:14px;line-height:1.45;color:var(--ink)}
.t-arrow{top:2850px;width:44px;height:44px;border-radius:50%;display:flex;align-items:center;justify-content:center}
.t-dots{left:572px;top:2964px;display:flex;gap:8px}
.t-dots i{width:10px;height:10px;border-radius:50%;background:#9ab8cf}
.t-dots i.on{background:var(--blue)}

/* faq */
.faq h2{left:0;top:3226px;width:1200px;text-align:center;font-size:46px;font-weight:400;color:var(--navy)}
.faq h2 b{font-weight:600}
.faq-open{left:232px;top:3320px;width:720px;height:170px;background:var(--navy);color:var(--white);padding:32px 40px;clip-path:polygon(0 0,92% 0,100% 20%,100% 100%,8% 100%,0 80%)}
.faq-open h3{font-size:22px;font-weight:600}
.faq-open p{font-size:13px;color:#c4d0de;margin-top:16px;line-height:1.6;width:560px}
.faq-dot{left:918px;top:3316px;width:22px;height:22px;border-radius:50%;background:var(--blue)}
.faq-list{left:248px;top:3512px;width:704px;list-style:none}
.faq-list li{height:48px;display:flex;align-items:center;justify-content:space-between;font-size:19px;color:var(--ink);border-bottom:1px solid #e3e9f0;padding-left:40px;position:relative}
.faq-list li::before{content:"";position:absolute;left:4px;width:12px;height:12px;border-radius:50%;background:var(--sky);border:2px solid var(--blue)}
.faq-list li span{font-size:20px;color:var(--navy)}

/* footer */
.footer{left:0;top:3940px;width:1200px;height:468px;background:var(--navy);color:var(--white)}
.f-brand{left:120px;top:4090px;display:flex;flex-direction:column;align-items:center;gap:14px;font-size:26px;font-weight:600}
.f-brand .brand-mark{width:90px;height:90px;border-radius:8px}
.f-col{top:4050px;font-size:13px;color:#c4d0de}
.f-col h4{color:var(--white);font-size:16px;font-weight:600;margin-bottom:22px}
.f-col .item{display:flex;gap:10px;margin-bottom:18px;line-height:1.4}
.f-col .item i{width:14px;height:14px;border-radius:50%;background:var(--blue);margin-top:2px;flex:none}
.f-col .link{margin-bottom:16px}
.news-field{width:220px;height:38px;background:var(--white);display:flex;align-items:center;justify-content:space-between;padding-left:12px;color:#8897a8;font-size:12px}
.news-field b{width:40px;height:38px;background:var(--blue)}
.socials{display:flex;gap:14px;margin-top:22px}
.socials i{width:24px;height:24px;border-radius:50%;background:var(--white)}
.copyright{left:0;top:4364px;width:1200px;text-align:center;font-size:13px;color:#c4d0de;border-top:1px solid #233b5e;padding-top:14px}
</style>
</head>
<body>

<!-- hero -->
<div class="ph hero" role="img" aria-label="Technician cleaning a roof-top solar array beside a house under a clear sky"></div>
<div class="abs hero-shade"></div>
<div class="abs topbar">
  <span><svg width="12" height="12" viewBox="0 0 24 24" fill="#fff"><path d="M6.6 10.8a15 15 0 006.6 6.6l2.2-2.2a1 1 0 011-.25 11.4 11.4 0 003.6.57 1 1 0 011 1V20a1 1 0 01-1 1A17 17 0 013 4a1 1 0 011-1h3.5a1 1 0 011 1 11.4 11.4 0 00.57 3.6 1 1 0 01-.25 1z"/></svg>02 4860 3178</span>
  <span>info@brightpane.com.au</span>
  <span>English ▾</span>
  <span>⌕</span>
</div>
<header class="abs nav">
  <div class="brand"><span class="brand-mark"></span>BrightPane</div>
  <nav class="menu"><a>Home</a><a>Residential</a><a>Reseller Portal</a><a>Customer Portal</a><a>Partners</a><a>About Us</a><a>Contact Us</a></nav>
  <div class="btn-contact">Contact Us</div>
</header>
<h1 class="abs hero" style="background:none">&nbsp;</h1>
<div class="abs" style="left:0;top:0;width:1200px">
  <h1 class="abs" style="left:0;top:232px;width:1200px;text-align:center;color:#fff;font-weight:600;font-size:64px;line-height:1.1">Expert Cleaning Solutions<small style="display:block;font-size:44px;font-weight:400">for Maximum Efficiency &amp; Protection.</small></h1>
  <div class="abs" style="left:0;top:508px;width:1200px;text-align:center;color:#fff;font-size:28px;font-weight:500">Choose Your Service Below:</div>
</div>
<div class="abs choice gutter">Gutter Cleaning</div>
<div class="abs choice solar">Solar Panel Cleaning</div>

<!-- about -->
<div class="abs about-bg"></div>
<div class="abs about-tint"></div>
<div class="abs hex hex-frame"></div>
<div class="ph hex hex-photo-a" role="img" aria-label="Crew in hi-vis vests washing rows of solar panels"></div>
<div class="ph hex hex-photo-b" role="img" aria-label="Solar panels on a green field"></div>
<div class="abs hex hex-small" style="left:90px;top:1200px"></div>
<div class="abs hex hex-small" style="left:132px;top:1224px;background:var(--navy)"></div>
<div class="abs hex hex-small" style="left:90px;top:1248px;opacity:.6"></div>
<div class="abs eyebrow" style="left:616px;top:892px">About Us</div>
<h2 class="abs about-title">ABOUT <b>BrightPane</b></h2>
<div class="abs about-text">
  <p>BrightPane specialises in <b>solar panel and gutter cleaning</b> for residential, commercial and government properties. With years of experience, we help maximise solar efficiency and prevent costly gutter blockages.</p>
  <p>Our team is <b>fully insured and WHS-approved</b>, ensuring the highest standards of safety and compliance for every job.</p>
</div>
<div class="abs read-more">Read more <i></i></div>

<!-- quote -->
<div class="abs quote-band"></div>
<div class="abs quote-tab"></div>
<div class="abs quote-title">Request a Quote – Fast &amp; Obligation-Free</div>
<ul class="abs quote-list">
  <li><svg width="16" height="16" viewBox="0 0 16 16"><circle cx="8" cy="8" r="8" fill="#29b2e9"/><path d="M4.5 8.2l2.2 2.2 4.8-4.8" stroke="#fff" stroke-width="1.8" fill="none"/></svg>Residential &amp; Commercial</li>
  <li><svg width="16" height="16" viewBox="0 0 16 16"><circle cx="8" cy="8" r="8" fill="#29b2e9"/><path d="M4.5 8.2l2.2 2.2 4.8-4.8" stroke="#fff" stroke-width="1.8" fill="none"/></svg>Government &amp; Infrastructure</li>
  <li><svg width="16" height="16" viewBox="0 0 16 16"><circle cx="8" cy="8" r="8" fill="#29b2e9"/><path d="M4.5 8.2l2.2 2.2 4.8-4.8" stroke="#fff" stroke-width="1.8" fill="none"/></svg>Custom Maintenance Plans</li>
</ul>
<div class="abs connect">Connect With Us:</div>
<div class="abs connect-mail">✉ sales@brightpane.com.au</div>
<div class="abs offices">
  <div>Sydney:<span>☏ 02 7391 5083</span></div>
  <div>Canberra:<span>☏ 02 6172 8354</span></div>
</div>
<div class="ph worker" role="img" aria-label="Smiling technician in an orange hi-vis jacket holding a cleaning broom"></div>

<!-- portals -->
<div class="abs portals"></div>
<h2 class="abs" style="left:0;top:1906px;width:1200px;text-align:center;color:#fff;font-size:46px;font-weight:400">Customer &amp; <b style="font-weight:600">Reseller Portals</b></h2>
<div class="abs" style="left:0;top:1972px;width:1200px;text-align:center;color:#c4d0de;font-size:14px">Managing services and partnerships has never been easier.</div>
<div class="ph oct portal-img customer" role="img" aria-label="Customer using a laptop beside a solar panel"></div>
<div class="ph oct portal-img reseller" role="img" aria-label="Two business partners reviewing plans in an office"></div>
<div class="abs portal-name" style="left:195px">Customer Portal</div>
<div class="abs portal-desc" style="left:195px">Track bookings, access reports, and manage<br>services effortlessly.</div>
<div class="abs portal-name" style="left:595px">Reseller Portal</div>
<div class="abs portal-desc" style="left:595px">Partner with us for exclusive benefits, priority<br>access, and business growth opportunities.</div>

<!-- testimonials -->
<div class="abs testi"></div>
<div class="abs testi-eyebrow">— Testimonial —</div>
<h2 class="abs" style="left:0;top:2570px;width:1200px;text-align:center;font-size:48px;font-weight:400;color:var(--navy)">What Our <b style="font-weight:600;color:var(--blue-dark)">Clients Say</b></h2>
<div class="abs oct t-card" style="left:240px">
  <div class="avatar" role="img" aria-label="Client portrait"></div>
  <h3>Tessa Holloway</h3>
  <p>Excellent service! They provided a detailed report and left our solar panels spotless</p>
</div>
<div class="abs oct t-card" style="left:630px">
  <div class="avatar" role="img" aria-label="Client portrait"></div>
  <h3>Lena Marsh</h3>
  <p>“Washing hands meant holding water bottle between your legs”</p>
</div>
<div class="abs t-arrow" style="left:160px;background:var(--blue)"><svg width="16" height="16" viewBox="0 0 16 16"><path d="M10 3L5 8l5 5" stroke="#fff" stroke-width="2" fill="none"/></svg></div>
<div class="abs t-arrow" style="left:996px;background:var(--navy)"><svg width="16" height="16" viewBox="0 0 16 16"><path d="M6 3l5 5-5 5" stroke="#fff" stroke-width="2" fill="none"/></svg></div>
<div class="abs t-dots"><i></i><i class="on"></i><i></i></div>

<!-- faq -->
<section class="faq">
  <h2 class="abs">Frequently Asked <b>Questions</b></h2>
  <div class="abs faq-open">
    <h3>Why is gutter cleaning important?</h3>
    <p>Gutters collect leaves and debris, leading to blockages that can cause water overflow and property damage. Regular cleaning ensures proper drainage and prevents costly repairs.</p>
  </div>
  <div class="abs faq-dot"></div>
  <ul class="abs faq-list">
    <li>What is vacuum roof gutter cleaning?<span>+</span></li>
    <li>How often should I have my gutters cleaned?<span>+</span></li>
    <li>Does rain clean solar panels and gutters?<span>+</span></li>
    <li>Will cleaning my solar panels improve their efficiency?<span>+</span></li>
    <li>Do you provide reports after cleaning?<span>+</span></li>
    <li>Are your cleaning methods safe for my property?<span>+</span></li>
    <li>Do you inspect for damage during cleaning?<span>+</span></li>
  </ul>
</section>

<!-- footer -->
<footer>
  <div class="abs footer"></div>
  <div class="abs f-brand" style="color:#fff"><span class="brand-mark"></span>BrightPane</div>
  <div class="abs f-col" style="left:420px;width:220px">
    <h4>Get In Touch With Us</h4>
    <div class="item"><i></i><div>Phone<br>02 7391 5083</div></div>
    <div class="item"><i></i><div>Email<br>info@brightpane.com.au</div></div>
    <div class="item"><i></i><div>Address<br>Head Office – Ferndale Rise NSW 2590<br>ABN: 48906237115</div></div>
  </div>
  <div class="abs f-col" style="left:680px;width:180px">
    <h4>Get In Touch With Us</h4>
    <div class="link">Home</div>
    <div class="link">About Us</div>
    <div class="link">Solar Cleaning</div>
    <div class="link">Gutter Cleaning</div>
    <div class="link">All Deal</div>
  </div>
  <div class="abs f-col" style="left:888px;width:240px">
    <h4>Subscribe to Our Newsletter</h4>
    <div class="news-field">Email Address<b></b></div>
    <div class="socials"><i></i><i></i><i></i></div>
  </div>
  <div class="abs copyright">Copyright ©2025 BrightPane – All Rights Reserved</div>
</footer>

</body>
</html>
```